Nimble Path Advert Flyer for TRIVENAPulses magazine

Nimble Path need a 1 A4 Full Page color advertisement created for the upcoming issues featured in the printed magazine. https://www.trivenapulse.com/magazines/September2017/BigData/

Nimblepath.com.au

Your trusted Data & Analytics Partner

Focused Data driven solutions & services provider
Proven experience and trusted technologies

Quorvanta
ZEL
Big Data
Cloud Architecture
Advanced Analytics

```html
<!DOCTYPE html>
<html lang="en">
<head>
<meta charset="UTF-8">
<title>Nimble Path – Data &amp; Analytics Partner Advert</title>
<link rel="stylesheet" href="https://fonts.googleapis.com/css2?family=Roboto:wght@300;400;500;700&family=Roboto+Condensed:wght@400;500&display=swap">
<style>
  :root {
    --sky-blue: #1f5fd6;
    --night: #050608;
    --orange: #f0772b;
    --white: #ffffff;
    --navy: #27306e;
    --rule: #9a9a9a;
  }
  * { box-sizing: border-box; margin: 0; padding: 0; }
  html, body {
    width: 704px; height: 1200px; overflow: hidden;
    background: var(--night);
    font-family: "Roboto", Arial, sans-serif;
  }
  .advert {
    position: relative; width: 704px; height: 1200px; overflow: hidden;
    background: var(--night);
  }
  .hero-photo {
    position: absolute; inset: 0 0 70px 0;
    background:
      radial-gradient(ellipse 340px 300px at 10% 40%, rgba(250,230,185,0.95), rgba(230,180,150,0.55) 45%, rgba(0,0,0,0) 75%),
      radial-gradient(ellipse 300px 200px at 20% 62%, rgba(120,95,100,0.7), rgba(0,0,0,0) 80%),
      linear-gradient(180deg, var(--sky-blue) 0%, #3f7be0 18%, #6f8fd8 32%, #5a5a78 50%, #1a1a22 62%, var(--night) 75%);
  }
  .brand {
    position: absolute; top: 62px; left: 48px;
  }
  .brand-name {
    font-family: "Roboto", Arial, sans-serif;
    font-weight: 700; font-size: 50px; letter-spacing: -0.5px;
    color: var(--navy); line-height: 1;
  }
  .headline {
    position: absolute; right: 40px; top: 470px; text-align: right;
    color: var(--white); font-weight: 400;
  }
  .headline-your {
    font-family: "Roboto", Arial, sans-serif; font-weight: 400;
    font-size: 74px; line-height: 1;
  }
  .headline-trusted {
    font-family: "Roboto Condensed", Arial, sans-serif; font-weight: 400;
    font-size: 56px; line-height: 1.1; color: var(--orange);
  }
  .headline-partner {
    font-family: "Roboto", Arial, sans-serif; font-weight: 300;
    font-size: 42px; line-height: 1.15; letter-spacing: 0.5px;
  }
  .positioning {
    position: absolute; right: 40px; top: 735px; text-align: right;
    color: var(--white); font-size: 17px; font-weight: 400; line-height: 1.35;
  }
  .positioning p:last-child {
    border-bottom: 1px solid var(--rule); padding-bottom: 4px;
  }
  .capabilities {
    position: absolute; right: 40px; top: 868px; list-style: none;
  }
  .capability {
    display: flex; justify-content: flex-end; align-items: center; gap: 8px;
    height: 38px; color: var(--white); font-size: 19px; font-weight: 500;
  }
  .capability span { border-bottom: 1px solid var(--rule); padding-bottom: 3px; }
  .capability svg { width: 18px; height: 18px; flex: none; }
  .web-band {
    position: absolute; left: 0; right: 0; bottom: 34px; height: 38px;
    background: var(--white);
    display: flex; align-items: center; justify-content: center;
    color: var(--navy); font-size: 15px; font-weight: 700; letter-spacing: 3px;
  }
</style>
</head>
<body>
<main class="advert">
  <div class="hero-photo" role="img" aria-label="Silhouette of a climber reaching down to help another up a mountain summit against a blue sunrise sky"></div>

  <header class="brand">
    <div class="brand-name">Nimble Path</div>
  </header>

  <h1 class="headline">
    <div class="headline-your">Your</div>
    <div class="headline-trusted">Trusted Data &amp;</div>
    <div class="headline-partner">ANALYTICS PARTNER</div>
  </h1>

  <div class="positioning">
    <p>FOCUSED DATA DRIVEN SOLUTIONS &amp; SERVICES PROVIDER</p>
    <p>PROVEN EXPERIENCE &amp; TRUSTED TECHNOLOGIES</p>
  </div>

  <ul class="capabilities">
    <li class="capability"><span>QUORVANTA</span>
      <svg viewBox="0 0 18 18"><rect x="3" y="3" width="12" height="12" fill="var(--orange)"/></svg></li>
    <li class="capability"><span>NUBRIX</span>
      <svg viewBox="0 0 18 18"><circle cx="9" cy="9" r="6" fill="none" stroke="var(--orange)" stroke-width="2"/></svg></li>
    <li class="capability"><span>ZEL</span>
      <svg viewBox="0 0 18 18"><rect x="5" y="3" width="8" height="12" fill="none" stroke="var(--orange)" stroke-width="2"/></svg></li>
    <li class="capability"><span>BIG DATA</span>
      <svg viewBox="0 0 18 18"><ellipse cx="9" cy="4" rx="6" ry="2.2" fill="var(--orange)"/><path d="M3 4v10c0 1.2 2.7 2.2 6 2.2s6-1 6-2.2V4" fill="var(--orange)"/><path d="M3 8.5c0 1.2 2.7 2.2 6 2.2s6-1 6-2.2" fill="none" stroke="var(--night)" stroke-width="1"/></svg></li>
    <li class="capability"><span>CLOUD ARCHITECTURE</span>
      <svg viewBox="0 0 18 18"><path d="M5 14h9a3 3 0 0 0 0-6 4.5 4.5 0 0 0-8.6-1A3.5 3.5 0 0 0 5 14z" fill="var(--orange)"/></svg></li>
    <li class="capability"><span>ADVANCE ANALYTICS</span>
      <svg viewBox="0 0 18 18"><rect x="2" y="12" width="3" height="4" fill="var(--orange)"/><rect x="6.5" y="9" width="3" height="7" fill="var(--orange)"/><rect x="11" y="5" width="3" height="11" fill="var(--orange)"/><rect x="15" y="2" width="2" height="14" fill="var(--orange)"/></svg></li>
  </ul>

  <footer class="web-band">www.nimblepath.com.au</footer>
</main>
</body>
</html>
```